Web Meeting Company Needs Bullet Point Icons for Power Point Presentation

I need 6 Icons / Buttons built to place into a power point presentation.

I have attached 2 slides. The first slide has the exsisting icons that we are using. On the next slide we need Icons that look similar to those in slide one, but reflect the discriptions that are listed next to the current Icons.

- Crowd Sourcing
- Kick Starters
- Segmentation
- Build A...
- Pop-Ups
- Gamification

On Slide 2 I have also uploaded a screen shot of some icons from GlimmerVault that i think would work from a symbol standpoint

Target Market(s)

Pharma Meeting Planning

Industry/Entity Type

It Company

Requirements
Must have
• Icons
Nice to have
• Icons
Should not have
• Icons

```html
<!DOCTYPE html>
<html lang="en">
<head>
<meta charset="utf-8">
<title>Meeting Services – Bullet Icons</title>
<link rel="stylesheet" href="https://fonts.googleapis.com/css2?family=Cinzel:wght@700&display=swap">
<style>
  :root {
    --bg-center: #8dab8c;
    --bg-mid: #6f8a80;
    --bg-edge: #4d6570;
    --ink: #17201c;
    --ink-glow: rgba(210, 225, 205, 0.55);
    --tile-shadow: rgba(30, 40, 40, 0.55);
    --glyph: #ffffff;
    --blue-a: #2a78c8;  --blue-b: #a7c6ee;
    --green-a: #148a45; --green-b: #6ff094;
    --purple-a: #5a1c92; --purple-b: #b57ef2;
    --red-a: #8a1010;   --red-b: #e02a2a;
    --yellow-a: #8f9200; --yellow-b: #f2f23a;
    --orange-a: #c44a08; --orange-b: #f7b04c;
  }
  * { margin: 0; padding: 0; box-sizing: border-box; }
  html, body { width: 1200px; height: 900px; overflow: hidden; }
  body {
    background: radial-gradient(ellipse 720px 620px at 620px 400px,
      var(--bg-center) 0%, var(--bg-mid) 60%, var(--bg-edge) 100%);
    position: relative;
    font-family: 'Cinzel', 'Times New Roman', serif;
  }
  .bullet-list { list-style: none; }
  .bullet {
    position: absolute;
    left: 274px;
    height: 110px;
    width: 700px;
  }
  .tile {
    position: absolute;
    left: 0; top: 0;
    width: 110px; height: 108px;
    border-radius: 8px;
    box-shadow: 4px 4px 0 var(--tile-shadow);
    overflow: hidden;
  }
  .tile::after {
    content: "";
    position: absolute;
    inset: 0;
    background: linear-gradient(135deg, rgba(255,255,255,0) 52%, rgba(255,255,255,0.22) 52%);
  }
  .tile svg { position: absolute; inset: 0; width: 110px; height: 108px; z-index: 1; }
  .tile--blue   { background: linear-gradient(45deg, var(--blue-a), var(--blue-b)); }
  .tile--green  { background: linear-gradient(45deg, var(--green-a), var(--green-b)); }
  .tile--purple { background: linear-gradient(45deg, var(--purple-a), var(--purple-b)); }
  .tile--red    { background: linear-gradient(45deg, var(--red-a), var(--red-b)); }
  .tile--yellow { background: linear-gradient(45deg, var(--yellow-a), var(--yellow-b)); }
  .tile--orange { background: linear-gradient(45deg, var(--orange-a), var(--orange-b)); }
  .label {
    position: absolute;
    left: 226px;
    font-size: 41px;
    font-weight: 700;
    letter-spacing: 1px;
    color: var(--ink);
    text-shadow: 2px 2px 1px var(--ink-glow), -1px -1px 0 rgba(0,0,0,0.15);
    white-space: nowrap;
  }
</style>
</head>
<body>
<ul class="bullet-list">
  <li class="bullet" style="top:62px">
    <div class="tile tile--blue">
      <svg viewBox="0 0 110 108" fill="none" stroke="var(--glyph)" stroke-width="4">
        <circle cx="55" cy="55" r="34"/>
        <ellipse cx="55" cy="55" rx="14" ry="34"/>
        <line x1="55" y1="21" x2="55" y2="89"/>
        <line x1="21" y1="55" x2="89" y2="55"/>
        <path d="M27 38 H83 M27 72 H83"/>
      </svg>
    </div>
    <span class="label" style="top:14px">~ Crowd Sourcing</span>
  </li>
  <li class="bullet" style="top:198px">
    <div class="tile tile--green">
      <svg viewBox="0 0 110 108">
        <g fill="var(--glyph)">
          <circle cx="50" cy="50" r="25"/>
          <g>
            <rect x="45" y="16" width="10" height="12"/>
            <rect x="45" y="72" width="10" height="12"/>
            <rect x="16" y="45" width="12" height="10"/>
            <rect x="72" y="45" width="12" height="10"/>
            <rect x="45" y="16" width="10" height="12" transform="rotate(45 50 50)"/>
            <rect x="45" y="72" width="10" height="12" transform="rotate(45 50 50)"/>
            <rect x="16" y="45" width="12" height="10" transform="rotate(45 50 50)"/>
            <rect x="72" y="45" width="12" height="10" transform="rotate(45 50 50)"/>
          </g>
        </g>
        <circle cx="50" cy="50" r="13" fill="var(--green-a)"/>
        <path d="M48 46 L80 80" stroke="var(--glyph)" stroke-width="9" stroke-linecap="round"/>
        <circle cx="46" cy="44" r="10" fill="var(--glyph)"/>
        <circle cx="41" cy="40" r="5" fill="var(--green-a)"/>
      </svg>
    </div>
    <span class="label" style="top:20px">~ Kick Starters</span>
  </li>
  <li class="bullet" style="top:334px">
    <div class="tile tile--purple">
      <svg viewBox="0 0 110 108">
        <g fill="var(--glyph)">
          <circle cx="40" cy="50" r="14"/>
          <circle cx="57" cy="40" r="18"/>
          <circle cx="74" cy="52" r="13"/>
          <rect x="26" y="50" width="62" height="14"/>
        </g>
        <path d="M36 66 L42 58 H68 L74 66 Z" fill="var(--glyph)" stroke="var(--purple-a)" stroke-width="2"/>
        <rect x="34" y="68" width="42" height="20" rx="2" fill="var(--glyph)"/>
        <rect x="40" y="76" width="20" height="4" fill="var(--purple-a)"/>
        <line x1="34" y1="70" x2="76" y2="70" stroke="var(--purple-a)" stroke-width="2"/>
      </svg>
    </div>
    <span class="label" style="top:22px">~ Segmentation</span>
  </li>
  <li class="bullet" style="top:468px">
    <div class="tile tile--red">
      <svg viewBox="0 0 110 108" fill="var(--glyph)">
        <path d="M38 42 L80 84" stroke="var(--glyph)" stroke-width="9" stroke-linecap="round"/>
        <path d="M22 34 L40 18 L54 26 L46 34 L50 40 L40 50 L34 44 L26 50 Z"/>
        <path d="M36 82 L72 46" stroke="var(--glyph)" stroke-width="9" stroke-linecap="round"/>
        <path d="M62 22 a16 16 0 0 1 22 22 l-6 -6 l-6 2 l-2 6 l6 6 a16 16 0 0 1 -22 -22 Z"/>
      </svg>
    </div>
    <span class="label" style="top:30px">~ Build A...</span>
  </li>
  <li class="bullet" style="top:602px">
    <div class="tile tile--yellow">
      <svg viewBox="0 0 110 108" fill="none" stroke="var(--glyph)">
        <path d="M28 62 V50 a27 27 0 0 1 54 0 V62" stroke-width="7"/>
        <rect x="22" y="56" width="14" height="26" rx="5" fill="var(--glyph)" stroke="none"/>
        <rect x="74" y="56" width="14" height="26" rx="5" fill="var(--glyph)" stroke="none"/>
        <path d="M80 82 L80 88 L58 92 H34" stroke-width="3"/>
        <line x1="34" y1="86" x2="34" y2="94" stroke-width="3"/>
      </svg>
    </div>
    <span class="label" style="top:38px">~ Pop-Ups</span>
  </li>
  <li class="bullet" style="top:738px">
    <div class="tile tile--orange">
      <svg viewBox="0 0 110 108">
        <path d="M32 36 H78 a12 12 0 0 1 12 12 L92 72 a8 8 0 0 1 -14 5 L70 66 H40 L32 77 a8 8 0 0 1 -14 -5 L20 48 a12 12 0 0 1 12 -12 Z" fill="var(--glyph)"/>
        <g fill="var(--orange-a)">
          <rect x="31" y="48" width="14" height="4"/>
          <rect x="36" y="43" width="4" height="14"/>
          <rect x="70" y="42" width="4" height="4"/>
          <rect x="64" y="48" width="4" height="4"/>
          <rect x="76" y="48" width="4" height="4"/>
          <rect x="70" y="54" width="4" height="4"/>
          <rect x="52" y="46" width="6" height="3"/>
        </g>
      </svg>
    </div>
    <span class="label" style="top:40px">~ Gamification</span>
  </li>
</ul>
</body>
</html>
```